R. T. HOLLOWAY, INC. is a US based Investment firm looking for a five-page website design.

Currently, their temporary site is located at: rtholloway.com and they would like to maintain the site design as much as possible.

R. T. HOLLOWAY, INC. sister companies are: Crestvale Lodge Investments (c-lodge.com) Benwick Petroleum (benwick-petroleum.com) and RTHF (rth-foundation.org/en)

Attached is a .ZIP file with designs and assets we think will be useful for your proposal… Content for the site is attached on: rtholloway website content.docx Current temp website design is attached as: Coming Soon Website.zip .EPS Logo files attached as: rtholloway logos.zip Sample business card attached as: R T Holloway Business cards.eps Other assets, such as Fonts and background images attached as: Assets.zip

Target Market(s)

Investors

Industry/Entity Type

Investments

Number of Pages Required

5+ page

Requirements
Must have
• Contact Page with a form.

```html
<!DOCTYPE html>
<html lang="en">
<head>
<meta charset="utf-8">
<title>R. T. Holloway, Inc. — Home</title>
<link rel="stylesheet" href="https://fonts.googleapis.com/css2?family=Cinzel:wght@400;600&family=Open+Sans:ital,wght@0,400;0,600;0,700;0,800;1,400&family=Arimo:wght@400;700&display=swap">
<style>
:root{
  --navy:#222d3e;
  --gold:#b39c5a;
  --gold-dark:#a38a47;
  --ink:#333;
  --muted:#6c6c6c;
  --light:#f2f2f2;
  --white:#fff;
}
*{margin:0;padding:0;box-sizing:border-box}
html,body{width:1200px;height:3086px;overflow:hidden}
body{position:relative;font-family:"Open Sans",sans-serif;color:var(--ink);background:var(--white)}
.abs{position:absolute}
a{text-decoration:none;color:inherit}

/* header */
.site-header{position:absolute;left:0;top:0;width:1200px;height:110px;z-index:5}
.brand{position:absolute;display:flex;flex-direction:column;align-items:center}
.brand-mark{width:40px;height:40px;border:2px solid var(--gold);border-radius:50%}
.brand-name{font-family:"Cinzel",serif;font-weight:400;color:var(--navy);white-space:nowrap;margin-top:8px}
.site-header .brand{left:52px;top:12px}
.site-header .brand-name{font-size:19px}
.main-nav{position:absolute;top:38px;left:364px;font-size:11px;color:var(--navy);letter-spacing:.2px}
.main-nav a{position:absolute;white-space:nowrap}
.main-nav a.active{color:var(--gold)}
.main-nav a.active::after{content:"";position:absolute;left:0;right:0;top:20px;height:1px;background:var(--gold)}
.call{position:absolute;left:956px;top:24px;display:flex;align-items:center;gap:14px}
.call-text{font-size:13px;line-height:19px;color:var(--navy)}
.call-text strong{font-size:15px;font-weight:700}

/* hero */
.hero{position:absolute;left:0;top:0;width:1200px;height:713px;background:linear-gradient(180deg,#d4d6d9 0%,#e9eaec 45%,#f7f7f7 75%,#fff 100%)}
.hero h1{position:absolute;left:0;width:1200px;text-align:center;font-family:"Arimo",sans-serif;font-weight:700}
.hero .h-welcome{top:204px;font-size:64px;color:var(--navy);letter-spacing:1px}
.hero .h-name{top:276px;font-size:62px;color:var(--gold)}
.hero p{position:absolute;left:290px;width:620px;top:360px;text-align:center;font-size:15.5px;line-height:27px;color:#333}
.btn{position:absolute;display:flex;align-items:center;justify-content:center;font-family:"Cinzel",serif;font-size:16px;letter-spacing:.5px;color:var(--white)}
.btn-gold{background:var(--gold)}
.btn-outline{border:1px solid var(--white)}

/* vision band */
.vision{position:absolute;left:0;top:713px;width:1200px;height:652px;background:var(--navy)}
.vision-word{position:absolute;left:116px;top:170px;font-family:"Arimo",sans-serif;font-weight:700;font-size:190px;color:#2a3546;line-height:1}
.vision-quote{position:absolute;left:315px;width:570px;top:384px;text-align:center;font-style:italic;font-size:27px;line-height:38px;color:var(--white)}
.about-card{position:absolute;left:653px;top:561px;width:487px;height:472px;background:var(--gold);color:var(--white);z-index:3}
.about-card .eyebrow{position:absolute;left:66px;top:64px;font-size:15px}
.about-card h2{position:absolute;left:66px;top:88px;font-family:"Cinzel",serif;font-weight:400;font-size:40px;color:var(--navy);white-space:nowrap}
.about-card p{position:absolute;left:66px;top:154px;width:360px;font-size:12px;line-height:22.5px}

/* investment areas */
.section-eyebrow{position:absolute;font-size:15px;color:var(--gold);font-weight:600}
.section-title{position:absolute;font-family:"Cinzel",serif;font-weight:400;color:var(--navy)}
.area{position:absolute;width:300px}
.area-icon{position:absolute;width:66px;height:66px;border-radius:50%}
.area h3{font-size:17px;font-weight:600;color:var(--navy)}
.area p{font-size:11.5px;line-height:19px;color:var(--muted);margin-top:6px;width:195px}
.read-more{display:inline-block;margin-top:6px;font-family:"Cinzel",serif;font-size:14px;color:var(--gold);text-decoration:underline}
.read-more::after{content:"";display:inline-block;margin-left:6px;border-left:6px solid var(--gold);border-top:5px solid transparent;border-bottom:5px solid transparent}
.area.right{text-align:right}
.area.right p{margin-left:auto}

/* social */
.band{position:absolute;background:var(--gold)}
.social-photo{position:absolute;left:190px;top:2072px;width:341px;height:375px;border-radius:70px 0 70px 0;background:linear-gradient(160deg,#6b5844 0%,#4d5a3e 50%,#2f3a44 100%);z-index:2}
.social-text p{position:absolute;left:691px;top:2231px;width:330px;font-size:11.5px;line-height:21px;color:var(--muted)}

/* newsletter */
.nl-outline{position:absolute;left:140px;top:2550px;font-family:"Open Sans",sans-serif;font-weight:600;font-size:88px;color:transparent;-webkit-text-stroke:1.5px #8a8f98;line-height:1}
.nl-solid{position:absolute;left:140px;top:2633px;font-family:"Open Sans",sans-serif;font-weight:800;font-size:88px;line-height:1;background:linear-gradient(180deg,#5f6672,#161d29);-webkit-background-clip:text;background-clip:text;color:transparent}
.nl-sub{position:absolute;left:144px;top:2744px;font-size:15px;color:#555}
.nl-field{position:absolute;left:670px;top:2618px;width:376px;height:34px;border-bottom:1px solid #555;font-size:11px;color:#555}

/* footer */
.site-footer{position:absolute;left:0;top:2841px;width:1200px;height:245px;background:var(--navy);color:#cfd3da}
.site-footer .brand{left:60px;top:46px}
.site-footer .brand-name{font-size:21px;color:var(--white)}
.foot-contact{position:absolute;top:42px;display:flex;gap:12px}
.foot-icon{width:36px;height:36px;border:1.5px solid var(--gold);border-radius:50%;display:flex;align-items:center;justify-content:center;margin-top:6px;flex:none}
.foot-contact h4{font-size:11.5px;color:var(--white);font-weight:700;margin-bottom:6px}
.foot-contact p{font-size:11.5px;line-height:20px}
.foot-links{position:absolute;left:62px;top:155px;font-size:11.5px;color:var(--white)}
.foot-links span{margin:0 9px;color:#aab}
.copyright{position:absolute;left:62px;top:179px;font-size:11.5px;color:var(--white)}
.copyright b{color:var(--gold)}
</style>
</head>
<body>

<section class="hero">
  <div class="abs" role="img" aria-label="Grey-toned photo of a city skyline blended with hands signing a document and floating currency symbols" style="left:0;top:100px;width:1200px;height:613px;background:radial-gradient(ellipse at 30% 40%,rgba(170,172,176,.45),transparent 60%),radial-gradient(ellipse at 85% 30%,rgba(180,182,186,.4),transparent 55%)"></div>
  <h1 class="h-welcome">WELCOME TO</h1>
  <h1 class="h-name">R. T. HOLLOWAY, INC.</h1>
  <p>R. T. Holloway, Inc. helps develop into a great nation and, with assertiveness, stamp its footprint worldwide.</p>
  <a class="btn btn-gold" style="left:527px;top:432px;width:146px;height:41px" href="#">CONTACT US</a>
</section>

<header class="site-header">
  <div class="brand"><span class="brand-mark"></span><span class="brand-name">R. T. HOLLOWAY, INC.</span></div>
  <nav class="main-nav">
    <a class="active" style="left:0" href="#">HOME</a>
    <a style="left:54px" href="#">ABOUT US</a>
    <a style="left:132px" href="#">INVESTMENT AREAS</a>
    <a style="left:256px" href="#">SOCIAL RESPONSIBILITY</a>
    <a style="left:402px" href="#">CONTACT US</a>
  </nav>
  <div class="call">
    <svg width="42" height="42" viewBox="0 0 42 42"><circle cx="21" cy="21" r="19.5" fill="none" stroke="#b39c5a" stroke-width="2"/><path d="M14 13c1-1 2-1 3 0l2 3c.5 1 0 2-1 2.5 1 2.5 3 4.5 5.5 5.5.5-1 1.5-1.5 2.5-1l3 2c1 1 1 2 0 3-2 2-4 2-7 0-3-2-6-5-8-8-2-3-2-5 0-7z" fill="#b39c5a"/></svg>
    <div class="call-text">Call us on:<br><strong>+1 (000) 000 0000</strong></div>
  </div>
</header>

<section class="vision">
  <div class="vision-word">Vision</div>
  <p class="vision-quote">R. T. Holloway, Inc. is the Main Private investment company Working Towards the Diversification and Consolidation of National and Regional Economy</p>
  <svg class="abs" style="left:574px;top:565px" width="52" height="22" viewBox="0 0 52 22"><path d="M1 2l25 16L51 2M8 2l18 11L44 2" fill="none" stroke="#b39c5a" stroke-width="1.2"/></svg>
</section>

<div class="about-card">
  <span class="eyebrow">About Us</span>
  <h2>R.T Holloway</h2>
  <p>Based in Houston, Texas, R. T. Holloway, Inc. is an investment company, founded in 2010, with the purpose to foster endeavors for socioeconomic development, and create platforms for harnessing the potential of world resources, designed to meet the demands of the emerging markets. R. T. Holloway, Inc. functions as a vehicle that enables investments, with the goal of developing the multiple opportunities available.</p>
  <a class="btn btn-outline" style="left:66px;top:357px;width:146px;height:41px" href="#">LEARN MORE</a>
</div>

<!-- investment areas -->
<span class="section-eyebrow" style="left:0;width:1200px;text-align:center;top:1437px">What We Do</span>
<h2 class="section-title" style="left:0;width:1200px;text-align:center;top:1460px;font-size:42px">Investment Areas</h2>

<div class="area" style="left:62px;top:1552px"><div class="area-icon" role="img" aria-label="Solar panel icon photo" style="left:0;top:0;background:radial-gradient(circle,#5c6b82,#2c3648)"></div><div style="margin-left:76px"><h3>Energy</h3><p>R. T. Holloway, Inc. holds investment both in Exploration &amp; Production,</p><a class="read-more" href="#">Read More</a></div></div>
<div class="area" style="left:62px;top:1700px"><div class="area-icon" role="img" aria-label="Mining truck photo" style="left:12px;top:4px;width:54px;height:54px;background:radial-gradient(circle,#c49a6c,#6f5a48)"></div><div style="margin-left:76px"><h3>Mining</h3><p>R. T. Holloway, Inc. holds interests in the management of operations .</p><a class="read-more" href="#">Read More</a></div></div>
<div class="area" style="left:62px;top:1851px"><div class="area-icon" role="img" aria-label="Industrial plant photo" style="left:12px;top:4px;width:54px;height:54px;background:radial-gradient(circle,#8fa3bf,#3e5476)"></div><div style="margin-left:76px"><h3>Industry</h3><p>R. T. Holloway, Inc. holds investment in a paint manufacturing plant</p><a class="read-more" href="#">Read More</a></div></div>

<div class="area right" style="left:764px;top:1552px"><div class="area-icon" role="img" aria-label="Calculator and documents photo" style="left:308px;top:10px;width:54px;height:54px;background:radial-gradient(circle,#c7ced8,#4d5b70)"></div><div style="width:300px"><h3>Finance</h3><p>R. T. Holloway, Inc. serves as a plat form to capture foreign</p><a class="read-more" href="#">Read More</a></div></div>
<div class="area right" style="left:764px;top:1700px"><div class="area-icon" role="img" aria-label="Doctor photo" style="left:308px;top:4px;width:54px;height:54px;background:radial-gradient(circle,#dfe5ec,#6d87a4)"></div><div style="width:300px"><h3>Healthcare</h3><p>R. T. Holloway, Inc. is committed to develop an investment project</p><a class="read-more" href="#">Read More</a></div></div>
<div class="area right" style="left:764px;top:1851px"><div class="area-icon" role="img" aria-label="House photo" style="left:308px;top:4px;width:54px;height:54px;background:radial-gradient(circle,#e6e2de,#8c5a4a)"></div><div style="width:300px"><h3>Real Estate</h3><p>R. T. Holloway, Inc. We have in our portfolio the following projects</p><a class="read-more" href="#">Read More</a></div></div>

<svg class="abs" style="left:240px;top:1590px" width="600" height="330" viewBox="0 0 600 330">
  <path d="M3 51h106l61 41" fill="none" stroke="#b39c5a" stroke-width="1"/>
  <path d="M218 8L134 158l84 150M502 8l86 150-86 150" fill="none" stroke="#b39c5a" stroke-width="1"/>
  <circle cx="168" cy="92" r="6" fill="#222d3e"/>
  <circle cx="134" cy="158" r="6" fill="#fff" stroke="#b39c5a"/>
  <circle cx="173" cy="227" r="6" fill="#fff" stroke="#b39c5a"/>
  <circle cx="551" cy="92" r="6" fill="#fff" stroke="#b39c5a"/>
  <circle cx="586" cy="158" r="6" fill="#fff" stroke="#b39c5a"/>
  <circle cx="546" cy="227" r="6" fill="#fff" stroke="#b39c5a"/>
</svg>
<div class="abs" role="img" aria-label="Two business people seated in armchairs in front of a gold double-chevron shape, seen from above" style="left:395px;top:1610px;width:410px;height:300px;background:linear-gradient(90deg,#b39c5a 0,#c8b47a 30%,#3a3c42 50%,#c8b47a 70%,#b39c5a 100%);clip-path:polygon(12% 0,88% 0,100% 50%,88% 100%,12% 100%,0 50%)"></div>

<!-- social responsibility -->
<div class="band" style="left:0;top:2174px;width:599px;height:113px"></div>
<div class="band" style="left:1058px;top:2174px;width:142px;height:113px"></div>
<div class="social-photo" role="img" aria-label="Several cupped hands holding soil with young green seedlings"></div>
<div class="social-text">
  <span class="section-eyebrow" style="left:691px;top:2100px;font-weight:400">Why Us</span>
  <h2 class="section-title" style="left:691px;top:2126px;font-size:40px;line-height:42px">Social<br>Responsibility</h2>
  <p>Since the commencement of our activity, R. T. Holloway, Inc. contributes to change the quality of life of children and seniors across the world, providing them with support for primary education and basic medical aid, which we believe to be the right of every human being.</p>
</div>
<a class="btn btn-gold" style="left:691px;top:2355px;width:146px;height:41px" href="#">LEARN MORE</a>

<!-- newsletter -->
<div class="nl-outline">Newsletter</div>
<div class="nl-solid">Signup !</div>
<div class="nl-sub">Stay upto date with R. T. HOLLOWAY, INC</div>
<div class="nl-field"><span style="position:absolute;left:2px;top:4px">Enter Email *</span>
  <svg style="position:absolute;right:8px;top:6px" width="20" height="16" viewBox="0 0 20 16"><rect x="1" y="1" width="18" height="14" fill="none" stroke="#333" stroke-width="1.4"/><path d="M1 1l9 8 9-8M1 15l7-6M19 15l-7-6" fill="none" stroke="#333" stroke-width="1.4"/></svg>
</div>
<a class="btn btn-gold" style="left:914px;top:2665px;width:131px;height:40px" href="#">SUBSCRIBE</a>

<footer class="site-footer">
  <div class="brand"><span class="brand-mark"></span><span class="brand-name">R. T. HOLLOWAY, INC.</span></div>
  <div class="foot-contact" style="left:535px">
    <span class="foot-icon"><svg width="16" height="16" viewBox="0 0 16 16"><path d="M8 1a5 5 0 0 1 5 5c0 4-5 9-5 9S3 10 3 6a5 5 0 0 1 5-5z" fill="#b39c5a"/><circle cx="8" cy="6" r="2" fill="#222d3e"/></svg></span>
    <div><h4>R. T. HOLLOWAY, INC</h4><p>2210 Larkmoor Ave. 12th floor<br>Houston, TX 77019</p></div>
  </div>
  <div class="foot-contact" style="left:757px">
    <span class="foot-icon"><svg width="16" height="16" viewBox="0 0 16 16"><path d="M3 2c1-1 2-1 2.5 0l1.5 2.5c.3.8 0 1.5-.8 2 .8 2 2.3 3.5 4.3 4.3.5-.8 1.2-1.1 2-.8L15 11.5c1 .5 1 1.5 0 2.5-1.5 1.5-3.5 1.5-6-.5S4 9 2.5 6.5C1 4 1.5 3 3 2z" fill="#b39c5a"/></svg></span>
    <div><h4>Phone :</h4><p style="font-size:13px">+1 (000) 000 0000</p></div>
  </div>
  <div class="foot-contact" style="left:939px">
    <span class="foot-icon"><svg width="16" height="12" viewBox="0 0 16 12"><rect width="16" height="12" rx="1" fill="#b39c5a"/><path d="M0 1l8 6 8-6" fill="none" stroke="#222d3e" stroke-width="1.3"/></svg></span>
    <div><h4>Email :</h4><p style="font-size:13px">name@rtholloway.com</p></div>
  </div>
  <div class="foot-links">Home<span>|</span>About Us<span>|</span>Investment Areas<span>|</span>Social Responsibility<span>|</span>Contact Us</div>
  <div class="copyright">©<b>R. T. HOLLOWAY, INC</b> - 2021 All rights reserved.</div>
</footer>

</body>
</html>
```